Taking a Paper and turning into a wonderful White Paper for Prospects and Clients

This is a white paper I need designed. I am including my company brochure so you can see the design/fonts being used and I'm including a white paper created - one that I like very much.

I am "NOT" looking for a cookie cutter white paper. I'm looking for a nice, clean design but with some creativity. Check out the white paper I included and you will get the idea.

Also included:
- the paper to be designed
- the paper to be designed "WITH" suggested design features such as carve outs, call outs and such

A few things I "DO NOT" like:
- images that are cheesy or corny
* people sitting at a table in a meeting
* Buildings

The white paper I included did not use pictures but had more design created by the firm. I like this approach and will probably give something like this more weight but is not required.
Updates

Reason: Realized time frame was too tight

Target Market(s)

Higher-End, wealthier clients

Industry/Entity Type

It Company

Requirements
Must have
• I DO NOT want the copy to be bunched together. The layout should flow where the copy is broken in the right spots to make reading easier. If you read a paper and it is just copy, interest is lost by everyone.
• COLORS: you can see from what I have included the colors I use
• My preference are very balanced colors using "clean spacing"

```html
<!DOCTYPE html>
<html lang="en">
<head>
<meta charset="utf-8">
<title>White Paper Spread – A Cautionary Tale</title>
<link href="https://fonts.googleapis.com/css2?family=Lato:wght@400;700&display=swap" rel="stylesheet">
<style>
  :root {
    --backdrop: #bcd0e4;
    --navy: #1c2452;
    --navy-soft: #252e60;
    --body-text: #d3d7e6;
    --photo-light: #e4e4e4;
    --photo-mid: #9a9a9a;
    --photo-dark: #3a3a3a;
  }
  * { box-sizing: border-box; margin: 0; padding: 0; }
  html, body {
    width: 1200px; height: 900px; overflow: hidden;
    background: var(--backdrop);
  }
  .spread {
    position: absolute;
    left: 30px; top: 244px;
    width: 1140px; height: 412px;
    display: flex;
  }
  .page {
    position: relative;
    width: 570px; height: 412px;
    background: var(--navy);
    font-family: "Lato", sans-serif;
    color: var(--body-text);
    font-size: 9.3px;
    line-height: 1.24;
  }
  .page--left {
    display: grid;
    grid-template-columns: repeat(3, 160px);
    column-gap: 11px;
    padding: 33px 0 0 33px;
    background: linear-gradient(90deg, var(--navy) 0%, var(--navy) 92%, var(--navy-soft) 100%);
  }
  .page--right {
    display: flex;
    background: linear-gradient(90deg, var(--navy-soft) 0%, var(--navy) 8%);
  }
  .text-column p { margin-bottom: 7px; }
  .page--right .text-column {
    width: 200px;
    padding: 33px 17px 0 35px;
  }
  .photo-panel {
    flex: 1;
    height: 100%;
    background: linear-gradient(180deg,
      var(--photo-light) 0%, #d2d2d2 22%, var(--photo-mid) 40%,
      var(--photo-dark) 52%, var(--photo-mid) 64%, #cfcfcf 82%, var(--photo-light) 100%);
  }
</style>
</head>
<body>
  <main class="spread">
    <section class="page page--left">
      <div class="text-column">
        <p>Let us now tell you a cautionary tale. This story illustrates some eventual pitfalls of choosing financial advisors based solely on whether they work under the fiduciary standard.</p>
        <p>Three sports stars – professional baseball pitchers Ray Dunmore and Jake Pellman, and pro football quarterback Mike Sorrento – believed they were bringing their “A-game” to the search for a great, trustworthy financial advisor.</p>
        <p>Vic Harlow, the financial advisor they chose, seemed to be made of all the right stuff. He worked for the Dallas-based Crestline Wealth Advisors. According to his business bios and cards, he was a Certified Public Account. The Pro Football Players Guild had endorsed him. Furthermore, he regularly attended the same church as Sorrento and had an interest in charity work.</p>
      </div>
      <div class="text-column">
        <p>Vic Harlow, nonetheless, turned out to be ruinously unscrupulous. He was not, in fact, a CPA. By fraudulent means, he transferred money out of his clients’ accounts, often without their consent, into The Seat Exchange, a financially-distressed company. And as a Seat Exchange board member, Harlow had multiple, egregious conflicts of interest that he never disclosed to his clients. By the time the deceitful scheme was uncovered and stopped, Harlow had misdirected $33 million of the three athletes’ money and nearly all of it was lost.</p>
        <p>One crucial fact got left out of most of the reporting on that story, namely, that Vic Harlow was a fiduciary.</p>
        <p>As a Registered Investment Advisor working through Crestline Capital Management, Harlow</p>
      </div>
      <div class="text-column">
        <p>was legally required to put his clients’ interests before his own and to act in their best interests. He failed to do that. Subsequently, the Security and Exchange Commission’s federal case against him was settled without his clients being fully reimbursed.</p>
        <p>Was this avoidable? Norvane tells you “Yes, this was avoidable.” What happened to Mike Sorrento does not have to happen to you. Norvane pro-actively verifies that your financial advisors are consistently acting in your best interest.</p>
        <p>The fine points in the differences between “the fiduciary standard” and “the suitability standard” are important for all of us to know, to be sure, but what’s most important for now is to understand that the mere fact of an adviser being a fiduciary does not guarantee that the adviser will do the right things for you.</p>
      </div>
    </section>
    <section class="page page--right">
      <div class="text-column">
        <p>After all, on the surface, Vic Harlow seemed like a trustworthy professional. He said he was a Certified Public Accountant. He worked through Crestline Wealth Advisers. He was endorsed by the Pro Football Players Guild. And he regularly attended the same church as Mike Sorrento. Had you asked him “Are you a fiduciary?” he would have said “Yes.”</p>
        <p>Norvane understands the daunting challenges investors face in trying to verify that their current, or potential future financial advisers are trustworthy. Our deep, broad knowledge of the field allowed us to develop our world-class system for auditing your financial advisors. Here is a sampling of the steps we would have taken, had Mike Sorrento been our client:</p>
      </div>
      <div class="photo-panel" role="img" aria-label="Black and white photograph of a mountain range reflected in a still lake, with pine trees along the shore"></div>
    </section>
  </main>
</body>
</html>
```